Sunvale Energy UK Flyer Design, for local domestic and commercial properties.

We are a renewable energy company called "SUNVALE ENERGY UK" we specialize in
Electrical and renewable energy project consultancy.
Solar panel installations
battery storage.
Electrical design and installation from Stage 3

Details can be found on our website: www.sunvaleenergyuk.co.uk
Am looking to have a flyer designed so we can have printed and delivered to all local areas.
We carry out free project surveys and offer full project transparency through out the clients journey.
attached is our logo of which i hope may help.

Target Market(s)

Domestic and commercial properties looking to dramatically reduce energy bills

Industry/Entity Type

Domestic, commercial, industrial, mixed used development and much more.

Font styles to use
Serif
Sans Serif
Decorative

Colors
FFC000
F8CF3A
FAE287
FDF2CF
FEFAEE
F0912C
F2A743
F7CA91
FBE8D2
FDF5EE
EE7325
F08F49
F5BC92
FAE3D3
FDF4ED

Requirements
Must have
• Highlight we offer free quotations and offer a fully transparent project processes from design, installation Plus leading health and safety process no matter what size project.
Nice to have
• Pictures of solar panel systems, i have attached a few pictures which you may wish to edit or take snippets etc.

```html
<!DOCTYPE html>
<html lang="en">
<head>
<meta charset="utf-8">
<title>Sunvale Energy UK Flyer</title>
<link href="https://fonts.googleapis.com/css2?family=Poppins:wght@300;400;600;700;800&display=swap" rel="stylesheet">
<style>
  :root{
    --yellow:#f2b01e;
    --yellow-bright:#ffc000;
    --orange:#ee7325;
    --ink:#141414;
    --paper:#f2f2f2;
    --backdrop:#e4e1dc;
    --panel-dark:#2e343c;
    --panel-mid:#5b636d;
    --sky:#5fc6f0;
  }
  *{box-sizing:border-box;margin:0;padding:0}
  html,body{width:1200px;height:1200px;overflow:hidden}
  body{background:var(--backdrop);font-family:"Poppins",sans-serif;color:var(--ink)}
  .flyer{position:absolute;left:180px;top:6px;width:840px;height:1188px;background:var(--paper);overflow:hidden}
  .flyer-art{position:absolute;inset:0;width:840px;height:1188px}
  .brand{position:absolute;left:300px;top:520px;display:flex;align-items:center;gap:16px}
  .brand-dot{width:54px;height:54px;border-radius:50%;background:var(--orange)}
  .brand-name{font-weight:300;font-size:34px;letter-spacing:3px;color:var(--ink);line-height:1;white-space:nowrap}

  .content{position:absolute;left:240px;top:600px;width:580px;display:flex;flex-direction:column}
  .headline{font-weight:800;line-height:1.15;letter-spacing:-0.5px;white-space:nowrap}
  .headline-main{display:block;font-size:27px;color:var(--ink)}
  .headline-accent{display:block;font-size:36px;color:var(--yellow)}

  .promises{list-style:none;margin-top:18px;display:flex;flex-direction:column;gap:12px}
  .promise{display:flex;flex-direction:column;gap:6px}
  .promise-row{display:flex;align-items:center;gap:10px;font-weight:700;font-size:12.5px;line-height:1.2;white-space:nowrap}
  .promise-row svg{flex:none;width:18px;height:18px}
  .promise-bar{display:block;height:6px;border-radius:3px;background:var(--yellow);margin-left:28px}
  .promise-quote .promise-bar{width:540px}
  .promise-safety .promise-bar{width:480px}

  .cta{margin-top:22px;font-weight:800;font-size:24px;line-height:1.2;letter-spacing:-0.4px;white-space:nowrap}
  .cta-copy{margin-top:8px;font-size:15px;line-height:1.45;font-weight:400}

  .contact{position:absolute;height:40px;border-radius:20px;background:var(--yellow);display:flex;align-items:center;gap:12px;padding:0 22px 0 16px;font-size:17px;font-weight:400;color:var(--ink);white-space:nowrap}
  .contact svg{width:22px;height:22px;flex:none}
  .contact-web{left:262px;top:984px}
  .contact-mail{left:280px;top:1032px}
  .contact-place{left:298px;top:1080px}
  .contact-phone{left:316px;top:1128px}
</style>
</head>
<body>
<main class="flyer">
  <svg class="flyer-art" viewBox="0 0 840 1188" xmlns="http://www.w3.org/2000/svg">
    <defs>
      <linearGradient id="roofPanels" x1="0" y1="0" x2="1" y2="1">
        <stop offset="0" stop-color="#7d8590"/>
        <stop offset="0.5" stop-color="#5b636d"/>
        <stop offset="1" stop-color="#2e343c"/>
      </linearGradient>
      <linearGradient id="roofScene" x1="0" y1="0" x2="0" y2="1">
        <stop offset="0" stop-color="#5fc6f0"/>
        <stop offset="0.3" stop-color="#6a8aa0"/>
        <stop offset="0.65" stop-color="#3c4652"/>
        <stop offset="1" stop-color="#a86a55"/>
      </linearGradient>
      <linearGradient id="inverterWall" x1="0" y1="0" x2="1" y2="1">
        <stop offset="0" stop-color="#f1ece8"/>
        <stop offset="0.5" stop-color="#c99582"/>
        <stop offset="1" stop-color="#e7e4e0"/>
      </linearGradient>
    </defs>
    <polygon class="band" points="0,0 840,0 840,352 0,252" fill="#ffc000"/>
    <polygon class="photo-panels" role="img" aria-label="Photo of rooftop solar panel array" points="0,0 840,0 840,332 0,232" fill="url(#roofPanels)"/>
    <polygon class="band" points="0,238 360,300 344,460 0,752" fill="#f2b01e"/>
    <polygon class="photo-roof" role="img" aria-label="Photo of solar panels on a tiled house roof with scaffolding" points="0,258 338,318 322,452 0,724" fill="url(#roofScene)"/>
    <circle cx="440" cy="330" r="166" fill="#f2b01e"/>
    <circle class="photo-inverter" role="img" aria-label="Photo of an installed inverter and battery storage unit on a wall" cx="440" cy="330" r="150" fill="url(#inverterWall)"/>
  </svg>

  <div class="brand">
    <span class="brand-dot"></span>
    <span class="brand-name">SUNVALE ENERGY UK</span>
  </div>

  <section class="content">
    <h1 class="headline">
      <span class="headline-main">Unleash Clean Energy Day and Night!</span>
      <span class="headline-accent">Go Solar with Battery Storage!</span>
    </h1>

    <ul class="promises">
      <li class="promise promise-quote">
        <span class="promise-row">
          <svg viewBox="0 0 20 20"><rect x="3" y="2" width="14" height="16" rx="2" fill="none" stroke="#141414" stroke-width="2"/><path d="M6 7h8M6 10.5h8M6 14h6" stroke="#141414" stroke-width="1.8"/></svg>
          <span>we offer free quotations and offer a fully transparent project processes from design</span>
        </span>
        <span class="promise-bar"></span>
      </li>
      <li class="promise promise-safety">
        <span class="promise-row">
          <svg viewBox="0 0 20 20"><path d="M3 3l14 14M17 3L3 17" stroke="#141414" stroke-width="2.6" stroke-linecap="round"/><circle cx="4" cy="4" r="2.5" fill="#141414"/></svg>
          <span>installation and health and safety process no matter what size project.</span>
        </span>
        <span class="promise-bar"></span>
      </li>
    </ul>

    <h2 class="cta">Don't Wait! Secure Your Energy Future Today!</h2>
    <p class="cta-copy">Embrace solar energy with battery storage and experience the freedom of clean, sustainable power day and night.Contact us now to schedule a consultation and learn how our solar panel installation with battery storage can transform your energy usage.</p>
  </section>

  <div class="contact contact-web">
    <svg viewBox="0 0 24 24" fill="none" stroke="#141414" stroke-width="1.6"><circle cx="12" cy="12" r="9"/><path d="M3 12h18M12 3c3 3 3 15 0 18M12 3c-3 3-3 15 0 18"/></svg>
    <span>www.sunvaleenergyuk.co.uk</span>
  </div>
  <div class="contact contact-mail">
    <svg viewBox="0 0 24 24" fill="none" stroke="#141414" stroke-width="1.6"><rect x="3" y="6" width="18" height="12" rx="1.5"/><path d="M3 7l9 6 9-6"/></svg>
    <span>hello@sunvaleenergyuk.co.uk</span>
  </div>
  <div class="contact contact-place">
    <svg viewBox="0 0 24 24" fill="none" stroke="#141414" stroke-width="1.6"><path d="M12 21s-6-6.5-6-11a6 6 0 0 1 12 0c0 4.5-6 11-6 11z"/><circle cx="12" cy="10" r="2.3"/></svg>
    <span>examplecations</span>
  </div>
  <div class="contact contact-phone">
    <svg viewBox="0 0 24 24" fill="none" stroke="#141414" stroke-width="1.6"><path d="M5 4h3l2 5-2 1.5a11 11 0 0 0 5.5 5.5L15 14l5 2v3a2 2 0 0 1-2 2A15 15 0 0 1 3 6a2 2 0 0 1 2-2z"/></svg>
    <span>01234567890</span>
  </div>
</main>
</body>
</html>
```